Harwick Structure Works needs a Business card design and logo

We Need a business card design and logo for a Building & Construction business based in Melbourne. We work in both the Domestic & Commercial sector. We specialize in all aspects of building including extensions, Renovations, and alterations. Construction Management, Project Management, And labour hire

Industry/Entity Type

Business

```html
<!DOCTYPE html>
<html lang="en">
<head>
<meta charset="utf-8">
<title>Harwick Structure Works – Business Card</title>
<link href="https://fonts.googleapis.com/css2?family=Exo+2:wght@400;500;600&display=swap" rel="stylesheet">
<style>
  :root{
    --bg:#d9dcdf;
    --paper:#ffffff;
    --paper-shade:#f1f3f5;
    --blue:#1a8fdb;
    --blue-light:#29a3e6;
    --blue-dark:#1476c2;
    --ink:#222a33;
    --muted:#4a525a;
    --band:#2c2f33;
    --band-fold:#15171a;
  }
  *{margin:0;padding:0;box-sizing:border-box}
  html,body{width:1200px;height:898px;overflow:hidden;background:var(--bg)}
  .stage{position:relative;width:1200px;height:898px}
  .card{position:absolute;width:560px;height:320px;left:320px;overflow:hidden;
        box-shadow:0 10px 26px rgba(0,0,0,.22);background:var(--paper)}
  .card--back{top:90px}
  .card--front{top:488px}

  /* back */
  .back-band-left{position:absolute;left:0;top:0;width:110px;height:100%;background:var(--blue)}
  .back-center{position:absolute;left:110px;top:0;width:220px;height:100%;
        background:linear-gradient(90deg,var(--paper),var(--paper-shade));
        display:flex;align-items:center;justify-content:center}
  .back-band-right{position:absolute;left:330px;top:0;width:230px;height:100%;
        background:linear-gradient(135deg,var(--blue-light),var(--blue-dark))}

  .brand{display:flex;align-items:center;gap:8px}
  .brand-mark{width:12px;height:12px;background:var(--blue);flex:none}
  .brand-name{font-family:"Exo 2",Arial,sans-serif;font-weight:600;font-size:15px;color:var(--ink);white-space:nowrap}

  /* front */
  .front-white{position:absolute;left:0;top:0;width:320px;height:100%;background:var(--paper)}
  .front-blue{position:absolute;left:320px;top:0;width:240px;height:100%;
        background:linear-gradient(160deg,var(--blue-light),var(--blue-dark))}
  .front-logo{position:absolute;left:28px;top:76px}
  .front-logo .brand-name{font-size:17px}
  .name-band{position:absolute;left:272px;top:52px;width:288px;height:34px;background:var(--band);
        display:flex;align-items:center;padding-left:14px;gap:9px;
        font-family:"Exo 2",Arial,sans-serif;font-size:12px;letter-spacing:.08em;color:#fff;text-transform:uppercase}
  .name-band .divider{width:1px;height:15px;background:#fff}
  .name-band .role{font-size:10.5px}
  .band-fold{position:absolute;left:272px;top:86px;width:0;height:0;
        border-top:12px solid var(--band-fold);border-left:22px solid transparent}

  .contact{position:absolute;left:28px;top:178px;font-family:"Exo 2",Arial,sans-serif;font-size:10.5px;color:var(--muted);letter-spacing:.03em}
  .contact-address{line-height:1.35;margin-bottom:12px}
  .contact-list{list-style:none;display:flex;flex-direction:column;gap:5px}
  .contact-list li{display:flex;align-items:center;gap:7px}
  .contact-list svg{width:10px;height:10px;fill:var(--muted)}
</style>
</head>
<body>
<main class="stage">

  <section class="card card--back" aria-label="Card back">
    <div class="back-band-left"></div>
    <div class="back-center">
      <div class="brand"><span class="brand-mark"></span><span class="brand-name">Harwick Structure Works</span></div>
    </div>
    <div class="back-band-right"></div>
  </section>

  <section class="card card--front" aria-label="Card front">
    <div class="front-white"></div>
    <div class="front-blue"></div>

    <div class="front-logo">
      <div class="brand"><span class="brand-mark"></span><span class="brand-name">Harwick Structure Works</span></div>
    </div>

    <div class="name-band"><span class="person">Daniel Corrow</span><span class="divider"></span><span class="role">Financial Advisor</span></div>
    <div class="band-fold"></div>

    <div class="contact">
      <p class="contact-address">041.12th floor Hall<br>Queensbury Road LKG</p>
      <ul class="contact-list">
        <li><svg viewBox="0 0 10 10"><path d="M2 0.5l1.6 2-1 1.2c.6 1.3 1.5 2.2 2.8 2.8l1.2-1 2 1.6-1 1.9C4.5 9 1 5.5 0.5 1.5z"/></svg>013 482 5570</li>
        <li><svg viewBox="0 0 10 10"><path d="M3 0h4a1 1 0 0 1 1 1v8a1 1 0 0 1-1 1H3a1 1 0 0 1-1-1V1a1 1 0 0 1 1-1zm0 1.5v6h4v-6zM5 8.2a.5.5 0 1 0 0 1 .5.5 0 0 0 0-1z"/></svg>013 482 5571</li>
        <li><svg viewBox="0 0 10 10"><path d="M2.5 0h4l1 1v2.5h1.5v6H1v-6h1.5zm1 1v3h3V1.5zM2.5 6v1.5h5V6z"/></svg>013 482 5572</li>
        <li><svg viewBox="0 0 10 10"><path d="M0 2h10v6H0zm1 .8v.3l4 2.6 4-2.6v-.3z"/></svg>hello@harwickworks.com</li>
        <li><svg viewBox="0 0 10 10"><path d="M5 0a5 5 0 1 0 0 10A5 5 0 0 0 5 0zm0 1a4 4 0 0 1 0 8 4 4 0 0 1 0-8zM1.5 4.5h7v1h-7zM4.5 1.2h1v7.6h-1z"/></svg>www.harwickworks.com</li>
      </ul>
    </div>
  </section>

</main>
</body>
</html>
```